Web Site Redesign

We operate a data centre facility specialing in colocation and Fibre optic connectivity (i.e. point to point fibre services and internet over fibre).

We have an existing site located at www.norvalex.example however this is very very tired and requires a redesign. We are looking for a fresh new design that will be appealing to potential customers.

The Company name is Norva eX and the primary corporate colour is bright red with secondary colours of white, grey and black. Specific bright red can be seen in attached company logo.

Website needs to be modern, clean and professional representing our premium colocation and fibre provider branding.

Our company slogan is : safe. secure. reliable

We will provide feedback regardless of the quality of the design to ensure a better outcome for all parties.

Please feel free to contact us if you have any questions.

# The designer can use placeholder images or feel free to use any/all or none of the attached images
# The designer can use sample filler text

Target Market(s)

Technical IT Professionals as well C level executives (i.e. CEO's, CIO).

Industry/Entity Type

Internet

Requirements
Must have
• clean design
Nice to have
• A sidebar with two sections. 1 for current promo and 1 for "Let us call you back/contact you"
Should not have
• Clutter

```html
<!DOCTYPE html>
<html lang="en">
<head>
<meta charset="utf-8">
<title>Norva eX – Business Continuity</title>
<link href="https://fonts.googleapis.com/css2?family=Arimo:ital,wght@0,400;0,700;1,400&display=swap" rel="stylesheet">
<style>
:root{
  --red:#d22f31;
  --red-dark:#b92224;
  --page:#f2eeed;
  --white:#ffffff;
  --ink:#111111;
  --grey:#8a8a8a;
  --line:#e2dcdb;
  --black:#000000;
}
*{margin:0;padding:0;box-sizing:border-box}
html,body{width:1130px;height:1200px;overflow:hidden;background:var(--page);font-family:"Arimo",Arial,sans-serif;color:var(--ink)}
.site{position:relative;width:1130px;height:1200px}

.brand{position:absolute;left:113px;top:20px;width:110px;height:100px;display:flex;flex-direction:column;align-items:center;justify-content:flex-end}
.brand-mark{width:46px;height:46px;background:var(--red);margin-bottom:12px}
.brand-name{font-size:26px;color:var(--ink);font-weight:400;white-space:nowrap}

.tagline{position:absolute;left:247px;top:20px;width:310px}
.tagline .small{font-size:13px}
.tagline .big{font-size:31px;font-style:italic;letter-spacing:-0.5px;line-height:1}
.tagline .sub{font-size:13px;text-align:right;margin-top:2px}

.contact{position:absolute;right:110px;top:31px;text-align:right;font-size:11.5px;line-height:19px}
.contact div{display:flex;align-items:center;justify-content:flex-end;gap:7px}
.contact svg{display:block}

.nav{position:absolute;left:246px;top:94px;width:776px;height:35px;background:var(--red);display:flex;align-items:stretch}
.nav a{color:var(--white);text-decoration:none;font-size:13.5px;display:flex;align-items:center;justify-content:center}
.nav a.active{background:linear-gradient(#3a3a3a,#111);}

.banner{position:absolute;left:97px;top:133px;width:926px;height:94px;background:linear-gradient(90deg,var(--red) 0%,var(--red) 55%,#c9393a 68%,#d57060 100%);overflow:hidden}
.banner h1{position:absolute;left:24px;top:31px;font-size:29px;font-weight:400;font-style:italic;color:var(--white)}
.banner-photo{position:absolute;right:0;top:0;width:300px;height:94px;background:linear-gradient(90deg,rgba(60,50,48,0) 0%,#5b4d48 25%,#a9a09a 55%,#3d3533 80%,#c15a2a 100%)}

.crumbs{position:absolute;left:97px;top:235px;width:925px;height:24px;background:var(--white);border:1px solid var(--line);font-size:10.5px;display:flex;align-items:center;padding:0 11px}
.crumbs .here{color:var(--red);margin-right:6px}
.crumbs .date{margin-left:auto}

.content{position:absolute;left:97px;top:271px;width:715px;height:772px;background:var(--white);border:1px solid var(--line);font-size:11.4px;line-height:17px}
.content .photo{position:absolute;left:19px;top:17px;width:209px;height:124px;background:linear-gradient(135deg,#2d2b2a,#6d6660 50%,#c0662b 70%,#2a2827)}
.content h2{position:absolute;left:249px;top:19px;font-size:18px;font-weight:400;color:var(--red)}
.content .intro{position:absolute;left:249px;top:59px;width:448px}
.content .body{position:absolute;left:22px;top:170px;width:680px}
.content p{margin-bottom:17px}
.content h3{font-size:11.4px;font-weight:700;margin-bottom:17px}
.content h4{font-size:11.4px;font-weight:700}
.content ul{list-style:none;margin-bottom:17px}
.content li{position:relative;padding-left:20px}
.content li::before{content:"";position:absolute;left:5px;top:5px;width:7px;height:7px;border-radius:50%;background:var(--red)}

.partners{position:absolute;left:820px;top:271px;width:202px;height:328px;background:var(--white);border:1px solid var(--line);overflow:hidden}
.partners .ribbon{position:absolute;left:0;top:0}
.partner-list{position:absolute;left:18px;top:40px;width:172px;display:flex;flex-direction:column;gap:26px;align-items:flex-start}
.partner{display:flex;align-items:center;gap:8px;font-size:17px;color:#3a3a3a}
.partner .sq{width:14px;height:14px;background:var(--red);flex:none}

.footer-rule{position:absolute;left:97px;top:1051px;width:925px;height:3px;background:var(--black)}
.copyright{position:absolute;left:98px;top:1068px;font-size:10.5px;line-height:17px}
.copyright .links a{color:var(--red);text-decoration:none}
.copyright .links span{margin:0 6px}
.badges{position:absolute;left:752px;top:1067px;display:flex;gap:5px}
.badges a{width:64px;height:18px;display:flex;align-items:center;justify-content:center;color:var(--white);font-size:10.5px;text-decoration:none}
.badges .dark{background:var(--black)}
.badges .red{background:var(--red)}
</style>
</head>
<body>
<div class="site">
  <header>
    <div class="brand"><span class="brand-mark"></span><span class="brand-name">Norva eX</span></div>
    <div class="tagline">
      <div class="small">Norva's</div>
      <div class="big">Save, Secure &amp; Reliable</div>
      <div class="sub">Data Centre</div>
    </div>
    <div class="contact">
      <div>sales@norvalex.example
        <svg width="14" height="10" viewBox="0 0 14 10"><rect width="14" height="10" fill="#d22f31"/><path d="M0 0l7 5 7-5" stroke="#fff" fill="none"/></svg></div>
      <div>+1 555 010 2040
        <svg width="14" height="10" viewBox="0 0 14 10"><path d="M1 4c0-3 12-3 12 0v1h-3V4H4v1H1z" fill="#d22f31"/><rect x="3" y="5" width="8" height="5" fill="#d22f31"/></svg></div>
    </div>
    <nav class="nav">
      <a href="#" style="width:78px">Home</a>
      <a href="#" style="width:100px">About Us</a>
      <a href="#" style="width:92px">Facilities ▾</a>
      <a href="#" class="active" style="width:142px">Business Continuity</a>
      <a href="#" style="width:95px">Services ▾</a>
      <a href="#" style="width:80px">Partners</a>
      <a href="#" style="width:97px">Webmail</a>
      <a href="#" style="width:92px">Contact Us</a>
    </nav>
  </header>

  <section class="banner">
    <div class="banner-photo" role="img" aria-label="Close-up of rack-mounted server hardware"></div>
    <h1>Could you afford to lose ALL your critical data?</h1>
  </section>

  <div class="crumbs"><span class="here">You're Here :</span> Home :: Business Continuity<span class="date">Monday, August 16 2010</span></div>

  <main class="content">
    <div class="photo" role="img" aria-label="Orange fibre optic patch cables plugged into a network switch"></div>
    <h2>Business Continuity (Disaster Recovery)</h2>
    <p class="intro">No matter how safe and secure you feel right now, the stability of your entire organisation could be under serious threat! Whether a natural disaster such as fire or flood, or man made issue such as arson or theft, these disasters could cause untold damage to your IT infrastructure. Could your organisation continue to operate during these disasters?</p>
    <div class="body">
      <p>Without a robust Business Continuity plan in place the future of your business could be at stake!</p>
      <p>In today's networked world, your communications network is one of the most critical elements in your organisations ability to operate. Your IT infrastructure is at the core of your business. Have you considered how your organisation would manage without the IT Infra-structure? If disaster should strike, what would be the impact on your day-to-day operations if your network ceased to function? Could you handle hours / days of downtime? More importantly, could you afford the downtime?</p>
      <h3>What if?</h3>
      <ul>
        <li>Key commercial data was lost or destroyed.</li>
        <li>Internet access and email was no longer available?</li>
        <li>Your organisation website was down or had a virus infect it?</li>
        <li>Your remote offices lost their connections?</li>
      </ul>
      <h3>Having a Business Continuity plan in place is essential in today's IT Environment to:</h3>
      <ul>
        <li>Ensure the continuing viability of your business operations</li>
        <li>Significantly reduce the cost of downtime if disaster strikes</li>
        <li>Reduce data loss</li>
        <li>Avoid a damaged business reputation</li>
        <li>Reduce the financial impact of a disaster</li>
        <li>Protect your revenue streams</li>
        <li>Reduce exposure to loss of productivity</li>
        <li>Ensure your mission critical applications</li>
      </ul>
      <p>Norva eX can offer a number of options including:</p>
      <h4>Cold Business Continuity Site</h4>
      <p>A reserved area to be used as an alternative location to primesite if disaster strikes. Floor space and Rack space areas available.</p>
      <h4>Warm Business Continuity Site</h4>
      <p>An alternative processing site that is partially equipped with equipment needed to recover in the event of a disaster.</p>
      <h4>Hot Business Continuity Site</h4>
      <p>A full mirror of the systems at the prime site. Floor space and Rack Space available.</p>
    </div>
  </main>

  <aside class="partners">
    <svg class="ribbon" width="100" height="90" viewBox="0 0 100 90">
      <polygon points="0,62 0,86 90,0 66,0" fill="#d22f31"/>
      <text x="0" y="0" transform="translate(8,66) rotate(-43.5)" fill="#fff" font-family="Arimo, Arial, sans-serif" font-size="9">OUR PARTNERS</text>
    </svg>
    <div class="partner-list" style="top:60px">
      <div class="partner" style="margin-left:40px"><span class="sq"></span>Veltra Link</div>
      <div class="partner">Orbital Telecom</div>
      <div class="partner" style="margin-left:8px">Kestrel Advisory</div>
      <div class="partner" style="margin-left:24px"><span class="sq"></span>Quantia Data</div>
    </div>
  </aside>

  <footer>
    <div class="footer-rule"></div>
    <div class="copyright">
      <div>Copyright © 2010 by NorvaeX. All Right Reserved.</div>
      <div class="links"><a href="#">Term Of Use</a><span>|</span><a href="#">Privacy Policy</a><span>|</span><a href="#">Contact Us</a></div>
    </div>
    <div class="badges">
      <a href="#" class="dark">Facenote</a>
      <a href="#" class="dark">Chirper</a>
      <a href="#" class="red">XHTML</a>
      <a href="#" class="red">CSS</a>
    </div>
  </footer>
</div>
</body>
</html>
```